Redesign two student school awards

I need to redesign 2 students awards. I need the elements of the letterhead to be incorporated into the Student Awards. I have covered some of the letterhead elements to show just the 4 elements that need to be incorporated: school emblem, school name, "For so much, what shall we repay?", and the 3 coloured ribbon. The awards need to be in colour and the use of the 3 school colours - purple, yellow (gold) and chocolate brown,

I have upload the 2 awards the school presents to students (they are printed on A4 Paper). The first one is the:

(1) Year Adviser Award - this award needs to include the school name; the title: Year Adviser's Award; Award to; Name (where the word is deleted and the office staff type the students name or uploaded names which can be autofilled); for the following achievements; the year (which can be changed an include the day and month (but auto filled); Year Adviser (where the teacher signs their name - see lower left of the award; (also the 5 categories - School Service, Community Service , Sporting Achievements, Leadership, Academic Achievement (these 5 categories must be able to be deleted as a student may receive the Year Adviser's Award for 1 or 2 of the categories)

(2) Principal's Award - all elements of this award need to be included. In this example there's a fake name Luke Dawson - this is where the office staff type in the students name or hopefully upload a list of names that are auto filled. The 5 categories need to be retained e.g. School Service, Community Service etc (these can be fixed as they are not deleted; for the following achievements; the year (which can be changed an include the day and month (but auto filled); my name and title,

For the 2 student awards it would be good if the design is in a computer program where the office staff can auto fill students names.

The main goal is to redesign the 2 awards, whilst retaining current elements and include 4 of the elements from the letter head.

Target Market(s)

School students (12 years old to 18 years old)

Industry/Entity Type

Education

Font styles to use
Serif

Requirements
Must have
• The elements and school colours mentioned in the description. Would be helpful if the computer program it is contained in allows for auto fill of student names, date, and for the Year Advisers award any one of the five award categories can be removed. To be printed on A4 paper/card

Colours must contain the school colours as mentioned before and the 4 elements of the letterhead. I am trying to have all our communications and awards contain similar elements.

```html
<!DOCTYPE html>
<html lang="en">
<head>
<meta charset="utf-8">
<title>Student Awards – Year Adviser's Award and Principal's Award</title>
<link rel="stylesheet" href="https://fonts.googleapis.com/css2?family=Rubik:wght@700;800&family=Great+Vibes&family=Arimo:wght@400&display=swap">
<style>
  :root {
    --purple: #93378f;
    --brown: #3d0f17;
    --gold: #f6e500;
    --cream: #fffdf1;
    --title-band: #ead7e6;
    --category-band: #fff8c6;
    --rule: #8a6a6f;
    --backdrop-light: #dbbd98;
    --backdrop-dark: #b77c5b;
  }
  * { box-sizing: border-box; margin: 0; padding: 0; }
  html, body { width: 1200px; height: 840px; overflow: hidden; }
  body {
    background: linear-gradient(90deg, var(--backdrop-light), var(--backdrop-dark));
    font-family: "Arimo", Arial, sans-serif;
    color: var(--brown);
    position: relative;
  }
  .certificate {
    position: absolute;
    top: 62px;
    width: 506px;
    height: 715px;
    background: var(--cream);
    box-shadow: 0 2px 8px rgba(60, 30, 20, 0.35);
    overflow: hidden;
  }
  .certificate--adviser { left: 59px; }
  .certificate--principal { left: 638px; }

  .ribbon { position: absolute; left: 0; width: 506px; height: 64px; }
  .ribbon--top { top: 0; }
  .ribbon--bottom { bottom: 0; transform: scaleY(-1); }

  .school-name {
    position: absolute; left: 0; width: 100%;
    text-align: center;
    font-family: "Rubik", Arial, sans-serif;
    font-weight: 800;
    font-size: 17px;
    letter-spacing: 0.3px;
    color: var(--brown);
  }
  .title-band {
    position: absolute; left: 0; width: 100%; height: 71px;
    background: var(--title-band);
    display: flex; align-items: center; justify-content: center;
  }
  .award-title {
    font-family: "Rubik", Arial, sans-serif;
    font-weight: 800;
    font-size: 31px;
    color: var(--purple);
  }
  .school-mark {
    position: absolute; left: 0; width: 100%;
    display: flex; flex-direction: column; align-items: center; gap: 8px;
  }
  .school-mark__dot {
    width: 54px; height: 54px; border-radius: 50%;
    background: var(--purple);
  }
  .school-mark__name {
    font-family: "Rubik", Arial, sans-serif;
    font-weight: 800;
    font-size: 16px;
    letter-spacing: 2px;
    color: var(--purple);
  }
  .awarded-to, .achievements-intro {
    position: absolute; left: 0; width: 100%;
    text-align: center; font-size: 12.5px;
  }
  .awarded-to { top: 283px; }
  .achievements-intro { top: 387px; }
  .student-name {
    position: absolute; left: 0; width: 100%; top: 310px;
    text-align: center;
    font-family: "Great Vibes", cursive;
    font-size: 50px;
    line-height: 60px;
    color: var(--brown);
  }
  .name-rule {
    position: absolute; left: 92px; width: 322px; top: 374px;
    border-top: 1px solid var(--brown);
  }
  .category-band {
    position: absolute; left: 0; width: 100%; top: 420px; height: 118px;
    background: var(--category-band);
  }
  .rosette {
    position: absolute; top: 8px; width: 86px; height: 106px;
    margin-left: -43px;
  }
  .rosette__shape {
    position: absolute; left: 0; top: 0;
    display: block; width: 86px; height: 106px;
  }
  .rosette__label {
    position: absolute; left: 0; top: 0; width: 86px; height: 82px;
    display: flex; align-items: center; justify-content: center;
    text-align: center;
    color: #fff;
    font-size: 10px;
    line-height: 13px;
    letter-spacing: -0.2px;
  }
  .signature {
    position: absolute; left: 76px; top: 552px; width: 100px; height: 42px;
    background: radial-gradient(ellipse at center, rgba(61, 15, 23, 0.22), rgba(61, 15, 23, 0));
  }
  .signatory {
    position: absolute; top: 600px; text-align: center;
  }
  .signatory--left { left: 57px; width: 126px; }
  .signatory--right { left: 329px; width: 128px; }
  .signatory__name {
    font-size: 15px; padding-bottom: 2px;
    border-bottom: 1px solid var(--rule);
  }
  .signatory__role {
    font-size: 15px; color: var(--purple); padding-top: 4px;
  }
</style>
</head>
<body>

<svg width="0" height="0" style="position:absolute">
  <defs>
    <symbol id="ribbon-sweep" viewBox="0 0 506 64">
      <path fill="#f6e500" d="M0 6 C150 22 330 2 506 8 L506 18 C330 10 150 32 0 16 Z"/>
      <path fill="#93378f" d="M0 14 C160 34 330 4 506 16 L506 30 C330 16 150 44 0 34 Z"/>
      <path fill="#3d0f17" d="M0 30 C110 44 300 24 506 32 L506 38 C300 32 130 60 0 58 Z"/>
      <path fill="#f6e500" d="M250 30 C360 18 440 22 506 26 L506 29 C440 26 360 24 250 32 Z"/>
    </symbol>
    <symbol id="rosette-shape" viewBox="0 0 86 106">
      <path fill="#93378f" d="M22 62 L6 102 L22 95 L32 106 L44 72 Z"/>
      <path fill="#93378f" d="M64 62 L80 102 L64 95 L54 106 L42 72 Z"/>
      <circle cx="43" cy="41" r="40" fill="#3d0f17"/>
      <circle cx="43" cy="41" r="31" fill="#93378f" stroke="#f6e500" stroke-width="2.5"/>
    </symbol>
  </defs>
</svg>

<article class="certificate certificate--adviser">
  <svg class="ribbon ribbon--top" aria-hidden="true"><use href="#ribbon-sweep"/></svg>
  <div class="school-mark" style="top:66px">
    <span class="school-mark__dot"></span>
    <span class="school-mark__name">RIDGEVIEW</span>
  </div>
  <h2 class="school-name" style="top:166px">RIDGEVIEW MEMORIAL HIGH SCHOOL</h2>
  <div class="title-band" style="top:201px"><h1 class="award-title">Year Adviser’s Award</h1></div>
  <p class="awarded-to">Awarded to</p>
  <p class="student-name">Owen Harper</p>
  <div class="name-rule"></div>
  <p class="achievements-intro">for the following achievements:</p>
  <div class="category-band">
    <div class="rosette" style="left:73px"><svg class="rosette__shape" width="86" height="106" viewBox="0 0 86 106"><use href="#rosette-shape"/></svg><span class="rosette__label">School<br>Service</span></div>
    <div class="rosette" style="left:163px"><svg class="rosette__shape" width="86" height="106" viewBox="0 0 86 106"><use href="#rosette-shape"/></svg><span class="rosette__label">Community<br>Service</span></div>
    <div class="rosette" style="left:252px"><svg class="rosette__shape" width="86" height="106" viewBox="0 0 86 106"><use href="#rosette-shape"/></svg><span class="rosette__label">Sporting<br>Achievement</span></div>
    <div class="rosette" style="left:342px"><svg class="rosette__shape" width="86" height="106" viewBox="0 0 86 106"><use href="#rosette-shape"/></svg><span class="rosette__label">Leadership</span></div>
    <div class="rosette" style="left:431px"><svg class="rosette__shape" width="86" height="106" viewBox="0 0 86 106"><use href="#rosette-shape"/></svg><span class="rosette__label">Academic<br>Achievement</span></div>
  </div>
  <div class="signature" role="img" aria-label="Year Adviser's handwritten signature"></div>
  <div class="signatory signatory--left">
    <p class="signatory__name">Mr. Daniel Ford</p>
    <p class="signatory__role">Year Adviser</p>
  </div>
  <div class="signatory signatory--right">
    <p class="signatory__name">May 14th 2020</p>
    <p class="signatory__role">Date</p>
  </div>
  <svg class="ribbon ribbon--bottom" aria-hidden="true"><use href="#ribbon-sweep"/></svg>
</article>

<article class="certificate certificate--principal">
  <svg class="ribbon ribbon--top" aria-hidden="true"><use href="#ribbon-sweep"/></svg>
  <h2 class="school-name" style="top:63px">RIDGEVIEW MEMORIAL HIGH SCHOOL</h2>
  <div class="title-band" style="top:88px"><h1 class="award-title">Principal’s Award</h1></div>
  <div class="school-mark" style="top:180px">
    <span class="school-mark__dot"></span>
    <span class="school-mark__name">RIDGEVIEW</span>
  </div>
  <p class="awarded-to">Awarded to</p>
  <p class="student-name">Luke Dawson</p>
  <div class="name-rule"></div>
  <p class="achievements-intro">for the following achievements:</p>
  <div class="category-band">
    <div class="rosette" style="left:73px"><svg class="rosette__shape" width="86" height="106" viewBox="0 0 86 106"><use href="#rosette-shape"/></svg><span class="rosette__label">School<br>Service</span></div>
    <div class="rosette" style="left:163px"><svg class="rosette__shape" width="86" height="106" viewBox="0 0 86 106"><use href="#rosette-shape"/></svg><span class="rosette__label">Community<br>Service</span></div>
    <div class="rosette" style="left:252px"><svg class="rosette__shape" width="86" height="106" viewBox="0 0 86 106"><use href="#rosette-shape"/></svg><span class="rosette__label">Sporting<br>Achievement</span></div>
    <div class="rosette" style="left:342px"><svg class="rosette__shape" width="86" height="106" viewBox="0 0 86 106"><use href="#rosette-shape"/></svg><span class="rosette__label">Leadership</span></div>
    <div class="rosette" style="left:431px"><svg class="rosette__shape" width="86" height="106" viewBox="0 0 86 106"><use href="#rosette-shape"/></svg><span class="rosette__label">Academic<br>Achievement</span></div>
  </div>
  <div class="signature" role="img" aria-label="Principal's handwritten signature"></div>
  <div class="signatory signatory--left">
    <p class="signatory__name">Mr R. Ellison</p>
    <p class="signatory__role">Principal</p>
  </div>
  <div class="signatory signatory--right">
    <p class="signatory__name">May 14th 2020</p>
    <p class="signatory__role">Date</p>
  </div>
  <svg class="ribbon ribbon--bottom" aria-hidden="true"><use href="#ribbon-sweep"/></svg>
</article>

</body>
</html>
```